Harborview Skin & Tissue Diagnostics CPC postcard

Need a postcard advertising our dermatopathology consultative services, and in particular, our new MeetLoom-based online clinico-pathologic correlation service. Would like the postcard to be clean, professional, modern, with great fonts. I have attached a basic draft postcard and my picture. Please use these as a starting point, but feel free to improvise. Please also see our website, www.cutislens-diagnostics.example.

```html
<!DOCTYPE html>
<html lang="en">
<head>
<meta charset="utf-8">
<title>Harborview Skin & Tissue Diagnostics – CPC Postcard</title>
<link rel="stylesheet" href="https://fonts.googleapis.com/css2?family=Jost:ital,wght@0,300;0,400;1,300&family=Roboto+Condensed:ital,wght@1,400&display=swap">
<style>
  :root {
    --stage: #1f1f1f;
    --card: #ffffff;
    --brand-red: #e3232b;
    --ink: #231f20;
    --text: #3a3a3a;
    --muted: #555555;
    --tissue-a: #d98b9e;
    --tissue-b: #f1c6cf;
    --photo-a: #cdbf9a;
    --photo-b: #2d3340;
  }
  * { box-sizing: border-box; margin: 0; padding: 0; }
  html, body { width: 1200px; height: 1200px; overflow: hidden; }
  body { background: var(--stage); font-family: "Jost", sans-serif; font-weight: 300; color: var(--text); position: relative; }

  .postcard { position: absolute; background: var(--card); overflow: hidden; }

  /* Address side */
  .postcard--back { left: 419px; top: 28px; width: 727px; height: 558px; }
  .tissue-visual {
    position: absolute; left: 0; top: 0; width: 350px; height: 200px;
    background: linear-gradient(180deg, var(--tissue-a) 0%, var(--tissue-b) 55%, rgba(255,255,255,0) 100%);
  }
  .intro-copy {
    position: absolute; left: 12px; top: 172px; width: 328px;
    font-size: 16.4px; line-height: 21.2px; text-align: justify; color: var(--text);
  }
  .rule-red { position: absolute; left: 0; top: 456px; width: 350px; height: 6px; background: var(--brand-red); }
  .rule-ink { position: absolute; left: 0; top: 465px; width: 350px; height: 2px; background: var(--ink); }
  .back-brand { position: absolute; left: 365px; top: 40px; width: 180px; }
  .brand-name { font-family: "Jost", sans-serif; font-weight: 400; color: var(--ink); line-height: 1.15; }
  .brand-mark { display: inline-block; width: 12px; height: 12px; border-radius: 50%; background: var(--brand-red); margin-bottom: 6px; }
  .back-brand .brand-name { font-size: 15px; }
  .return-address { position: absolute; left: 365px; top: 146px; font-size: 15px; line-height: 18px; color: var(--muted); font-style: normal; }
  .stamp-box { position: absolute; left: 551px; top: 11px; width: 166px; height: 166px; border: 1.5px solid var(--ink); }

  /* Message side */
  .postcard--front { left: 64px; top: 612px; width: 728px; height: 560px; }
  .portrait {
    position: absolute; left: 0; top: 0; width: 299px; height: 360px;
    background: linear-gradient(180deg, var(--photo-a) 0%, #b9ab8a 45%, var(--photo-b) 100%);
  }
  .portrait-caption {
    position: absolute; left: 0; top: 334px; width: 304px; height: 28px; background: var(--card);
    font-family: "Roboto Condensed", sans-serif; font-style: italic; font-size: 16px; line-height: 28px;
    padding-left: 8px; color: var(--ink); white-space: nowrap; overflow: hidden;
  }
  .headline-panel {
    position: absolute; left: 305px; top: 0; width: 423px; height: 184px; background: var(--brand-red);
    display: flex; align-items: center; justify-content: center; text-align: center;
  }
  .headline { font-style: italic; font-weight: 300; font-size: 38px; line-height: 44px; color: #fff; }
  .service-panel {
    position: absolute; left: 305px; top: 190px; width: 423px; height: 178px; background: var(--ink);
    display: flex; align-items: center; justify-content: center; text-align: center;
  }
  .service-text { font-size: 31px; line-height: 40px; color: #fff; }
  .tagline-strip {
    position: absolute; left: 0; top: 370px; width: 728px; height: 40px;
    border-top: 1px solid #888; border-bottom: 1px solid #888; background: var(--card);
    font-size: 24px; line-height: 38px; padding-left: 10px; color: var(--ink); white-space: nowrap;
  }
  .contact-band {
    position: absolute; left: 0; top: 411px; width: 728px; height: 149px;
    background: linear-gradient(180deg, #ffffff 0%, #e4e4e4 100%);
  }
  .front-brand { position: absolute; left: 24px; top: 32px; width: 240px; }
  .front-brand .brand-name { font-size: 20px; }
  .contact-lead { position: absolute; left: 299px; top: 16px; font-size: 21px; line-height: 25px; color: var(--text); }
  .contact-line { position: absolute; left: 299px; display: flex; align-items: center; gap: 10px; font-size: 25px; color: var(--text); white-space: nowrap; }
  .contact-line--phone { top: 72px; }
  .contact-line--web { top: 108px; }
  .contact-line svg { width: 14px; height: 14px; }
  .contact-divider { width: 1px; height: 24px; background: #999; }
</style>
</head>
<body>
  <section class="postcard postcard--back">
    <div class="tissue-visual" role="img" aria-label="Microscope view of pink-stained skin tissue"></div>
    <p class="intro-copy">We know how important reliable dermatopathology services are to your patients and your practice. As your partner in patient care, we want to do our part in helping you arrive at the diagnosis for each patient you entrust to us. We also know that part of our job is making working with us as smooth as possible. We can provide courier pick up service to local practices, and we will help arrange overnight delivery for specimens sent from outside our area. We'll handle the details so you can focus on the care of your patients.</p>
    <div class="rule-red"></div>
    <div class="rule-ink"></div>
    <div class="back-brand">
      <span class="brand-mark"></span>
      <p class="brand-name">Harborview Skin &amp; Tissue Diagnostics</p>
    </div>
    <address class="return-address">1480 Harbor Crest Blvd.<br>Suite 210, Seaside Bay<br>CA 90000</address>
    <div class="stamp-box"></div>
  </section>

  <section class="postcard postcard--front">
    <div class="portrait" role="img" aria-label="Portrait of the dermatopathologist in a suit, arms crossed, in an office"></div>
    <p class="portrait-caption">Daniel R. Okafor, M.D., Dermatopathologist</p>
    <div class="headline-panel">
      <h1 class="headline">Like having a<br>dermatopathologist<br>in your office.</h1>
    </div>
    <div class="service-panel">
      <p class="service-text">MeetLoom-based, online<br>clinico-pathologic correlation<br>to clarify difficult cases.</p>
    </div>
    <p class="tagline-strip">Dedicated to the power of clinico-pathologic correlation (CPC).</p>
    <div class="contact-band">
      <div class="front-brand">
        <span class="brand-mark"></span>
        <p class="brand-name">Harborview Skin &amp; Tissue Diagnostics</p>
      </div>
      <p class="contact-lead">To find out more about our dermatopathology<br>consultation services, please call:</p>
      <p class="contact-line contact-line--phone">
        <svg viewBox="0 0 24 24" aria-hidden="true"><path fill="#e3232b" d="M6.6 10.8a15.1 15.1 0 0 0 6.6 6.6l2.2-2.2a1 1 0 0 1 1-.25 11.4 11.4 0 0 0 3.6.57 1 1 0 0 1 1 1V20a1 1 0 0 1-1 1A17 17 0 0 1 3 4a1 1 0 0 1 1-1h3.5a1 1 0 0 1 1 1c0 1.25.2 2.45.57 3.57a1 1 0 0 1-.25 1z"/></svg>
        <span class="contact-divider"></span>800.555.0148
      </p>
      <p class="contact-line contact-line--web">
        <svg viewBox="0 0 24 24" aria-hidden="true"><g fill="none" stroke="#e3232b" stroke-width="2"><circle cx="12" cy="12" r="9"/><ellipse cx="12" cy="12" rx="4" ry="9"/><path d="M3 12h18M5 7h14M5 17h14"/></g></svg>
        <span class="contact-divider"></span>www.cutislens-diagnostics.example
      </p>
    </div>
  </section>
</body>
</html>
```